Silver Hollow Works
innovative motorcycle accessories
Modern
Miles and Doreen Falkner
4/61 Tiverley Road
Bangalow NSW 2479 Australia
shw@silverhollowworks.example.au
www.silverhollowworks.example.au
the back of the business card will have different logos of all the products we sell. please see uploaded logos.
this is the logo which goes on the front of the card
this is 1 of 4 logos for the back of the business card
this is 2 of 4 logos for the back of the business card
this is 3 of 4 logos for the back of the business card
this is 4 of 4 logos for the back
this is 5 of 5 logos for the back. please try and make the SPEXTAB logo the same font as the BORTELLO logo.
zip file of logo in ai. format for SILVER HOLLOW WORKS
please add the words "Innovative Motorcycle Accessories to the front of the card

```html
<!DOCTYPE html>
<html lang="en">
<head>
<meta charset="utf-8">
<title>Silver Hollow Works – Stationery Set</title>
<link href="https://fonts.googleapis.com/css2?family=Montserrat:wght@700&family=Arimo:wght@400;700&display=swap" rel="stylesheet">
<style>
  :root{
    --backdrop:#c9c9c9;
    --paper:#ffffff;
    --ink:#111111;
    --band:#050505;
    --gold:#f2c21a;
    --gold-pale:#fbeeb8;
    --rule:#9a9a9a;
    --cell:#e4e4e4;
    --muted:#555555;
    --badge-blue:#2f5fa8;
    --badge-red:#c8342b;
    --badge-grey:#6b6b6b;
  }
  *{box-sizing:border-box;margin:0;padding:0}
  html,body{width:1200px;height:548px;overflow:hidden}
  body{background:var(--backdrop);position:relative;font-family:"Arimo",Arial,sans-serif;color:var(--ink)}

  .sheet,.card,.envelope{position:absolute;background:var(--paper);box-shadow:0 1px 3px rgba(0,0,0,.25);overflow:hidden}
  .header-band{position:absolute;left:0;top:0;width:100%;display:block}

  .brand{position:absolute;display:flex;align-items:center;gap:6px}
  .brand-dot{width:14px;height:14px;border-radius:50%;background:var(--gold);flex:none}
  .brand-name{font-family:"Montserrat",Arial,sans-serif;font-weight:700;color:#fff;font-size:9px;letter-spacing:.5px;line-height:1.1;white-space:nowrap}

  .contact{position:absolute;font-size:5.5px;line-height:8px;color:var(--muted)}
  .contact li{list-style:none;display:flex;align-items:center;gap:4px;white-space:nowrap}
  .contact li::before{content:"";width:4px;height:4px;background:var(--gold);flex:none}

  .watermark{position:absolute;left:110px;top:270px;width:150px;height:110px;border-radius:50%;background:radial-gradient(ellipse at center,var(--gold-pale),rgba(255,255,255,0) 70%)}

  /* fax sheet */
  .fax-label{position:absolute;right:44px;top:118px;font-size:7px;font-weight:700;letter-spacing:.5px}
  .fax-table{position:absolute;left:22px;top:128px;width:290px;border-collapse:collapse;font-size:5.5px}
  .fax-table td{border:1px solid var(--rule);height:17px;padding:0 4px}
  .fax-table .field{width:30px;background:var(--cell)}
  .fax-table .entry{width:115px}
  .fax-options{position:absolute;left:22px;top:224px;display:flex;gap:18px;font-size:5.5px}
  .fax-options span{display:flex;align-items:center;gap:3px}
  .fax-options span::before{content:"";width:6px;height:6px;border:1px solid var(--rule)}

  /* business card back */
  .card-back{left:787px;top:22px;width:148px;height:72px}
  .badge-grid{position:absolute;left:6px;top:9px;display:grid;grid-template-columns:42px 42px;column-gap:4px;row-gap:6px}
  .badge{display:flex;align-items:center;gap:2px;font-size:4.5px;font-weight:700;color:var(--ink);white-space:nowrap}
  .badge-mark{width:9px;height:7px;background:var(--badge-blue);flex:none}
  .badge-mark.red{background:var(--badge-red)}
  .badge-mark.dark{background:var(--band)}
  .badge-mark.grey{background:var(--badge-grey)}
  .card-tag{position:absolute;left:96px;top:10px;width:46px;font-size:4.5px;font-weight:700;line-height:6px;text-align:center}

  /* business card front */
  .card-front{left:955px;top:22px;width:175px;height:78px;background:var(--band)}
  .card-front .brand-name{font-size:6px}
  .card-front .brand-dot{width:10px;height:10px}
  .card-person{position:absolute;left:92px;top:40px;font-size:5px;font-weight:700;color:var(--gold);white-space:nowrap}
  .card-front .contact{color:#ddd;font-size:4.5px;line-height:6px}
</style>
</head>
<body>

<!-- Fax sheet -->
<section class="sheet fax-sheet" style="left:19px;top:19px;width:355px;height:519px">
  <svg class="header-band" width="355" height="112" viewBox="0 0 355 112">
    <rect width="355" height="112" fill="var(--band)"/>
    <path d="M140 112 Q270 86 355 8 V112 Z" fill="var(--paper)"/>
    <path d="M140 112 Q270 86 355 8" fill="none" stroke="var(--gold)" stroke-width="4"/>
  </svg>
  <div class="brand" style="left:16px;top:36px"><span class="brand-dot"></span><span class="brand-name">SILVER HOLLOW WORKS</span></div>
  <div class="fax-label">FAX</div>
  <table class="fax-table">
    <tr><td class="field">To:</td><td class="entry"></td><td class="field">From:</td><td class="entry"></td></tr>
    <tr><td class="field">Fax:</td><td class="entry"></td><td class="field">Pages:</td><td class="entry"></td></tr>
    <tr><td class="field">Phone:</td><td class="entry"></td><td class="field">Date:</td><td class="entry"></td></tr>
    <tr><td class="field">Re:</td><td class="entry"></td><td class="field">CC:</td><td class="entry"></td></tr>
  </table>
  <div class="fax-options"><span>Urgent</span><span>For Review</span><span>Please Comment</span><span>Please Reply</span><span>Please Recycle</span></div>
  <div class="watermark" role="img" aria-label="Faint brand mark in pale gold"></div>
  <ul class="contact" style="left:14px;top:468px">
    <li>4/61 Tiverley Road</li>
    <li>Bangalow NSW 2479 Australia</li>
    <li>P: 02 5550 1847</li>
    <li>shw@silverhollowworks.example.au</li>
    <li>www.silverhollowworks.example.au</li>
  </ul>
</section>

<!-- Letterhead -->
<section class="sheet letterhead" style="left:398px;top:19px;width:360px;height:519px">
  <svg class="header-band" width="360" height="112" viewBox="0 0 360 112">
    <rect width="360" height="112" fill="var(--band)"/>
    <path d="M140 112 Q275 86 360 8 V112 Z" fill="var(--paper)"/>
    <path d="M140 112 Q275 86 360 8" fill="none" stroke="var(--gold)" stroke-width="4"/>
  </svg>
  <div class="brand" style="left:16px;top:36px"><span class="brand-dot"></span><span class="brand-name">SILVER HOLLOW WORKS</span></div>
  <div class="watermark" style="left:105px;top:225px" role="img" aria-label="Faint brand mark in pale gold"></div>
  <ul class="contact" style="left:14px;top:468px">
    <li>4/61 Tiverley Road</li>
    <li>Bangalow NSW 2479 Australia</li>
    <li>P: 02 5550 1847</li>
    <li>shw@silverhollowworks.example.au</li>
    <li>www.silverhollowworks.example.au</li>
  </ul>
</section>

<!-- Business card back -->
<section class="card card-back">
  <div class="badge-grid">
    <span class="badge"><span class="badge-mark"></span>CAPSAFEX</span>
    <span class="badge"><span class="badge-mark dark"></span>TOVU</span>
    <span class="badge"><span class="badge-mark red"></span>KITBINDA</span>
    <span class="badge"><span class="badge-mark grey"></span>SPEXTAB</span>
    <span class="badge"><span class="badge-mark dark"></span>BORTELLO</span>
  </div>
  <div class="card-tag">innovative motorcycle accessories</div>
</section>

<!-- Business card front -->
<section class="card card-front">
  <svg class="header-band" width="175" height="78" viewBox="0 0 175 78">
    <path d="M70 0 Q135 4 175 28 V0 Z" fill="var(--paper)"/>
    <path d="M60 0 Q130 8 175 40" fill="none" stroke="var(--gold)" stroke-width="2"/>
  </svg>
  <div class="brand" style="left:8px;top:14px"><span class="brand-dot"></span><span class="brand-name">SILVER HOLLOW WORKS</span></div>
  <div class="card-person">Miles &amp; Doreen Falkner</div>
  <ul class="contact" style="left:92px;top:48px">
    <li>M: 0400 555 218</li>
    <li>shw@silverhollowworks.example.au</li>
    <li>www.silverhollowworks.example.au</li>
  </ul>
</section>

<!-- Envelope -->
<section class="envelope" style="left:782px;top:175px;width:370px;height:192px">
  <svg class="header-band" width="370" height="100" viewBox="0 0 370 100">
    <rect width="370" height="100" fill="var(--band)"/>
    <path d="M150 100 Q285 78 370 6 V100 Z" fill="var(--paper)"/>
    <path d="M150 100 Q285 78 370 6" fill="none" stroke="var(--gold)" stroke-width="4"/>
  </svg>
  <div class="brand" style="left:16px;top:34px"><span class="brand-dot"></span><span class="brand-name">SILVER HOLLOW WORKS</span></div>
  <ul class="contact" style="left:14px;top:136px">
    <li>4/61 Tiverley Road</li>
    <li>Bangalow NSW 2479 Australia</li>
    <li>P: 02 5550 1847</li>
    <li>shw@silverhollowworks.example.au</li>
    <li>www.silverhollowworks.example.au</li>
  </ul>
</section>

</body>
</html>
```